Gutschein für Fotograf
Designer PelaWix hat meinen Geschmack am besten getroffen, ging auf meine Änderungsvorschläge genau ein, und änderte Details zu meiner vollsten Zufriedenheit. Kann ich auf alle Fälle weiter empfehlen.
Zielgruppe
Ich bin Fotograf und suche nach einem Gutschein für meine Arbeiten. Zielgruppen sind Privatpersonen, Pärchenfotos, Hochzeit, Baby usw.
Aufgabenstellung
Der Gutschein sollte zu meiner Homepage passen und auch zu meinen Bildern/ meinem Stil.
Folgendes könnte darauf stehen: (Foto) Gutschein - einzulösen bei - meine Homepage sollte darauf sein - es sollte eine Version mit 50 € sein und eine mit 100€ geben. Mir gefällt wahrscheinlich etwas klassisches besser, aber auch retro/ vintage könnte ich mir gut vorstellen. Vor allem möchte ich aber, dass es weiblich/ feminin wirkt. Ob Bilder von mir auf dem Gutschein von Vorteil sind, kann ich leider nicht einschätzen, aber die Bilder können jederzeit von meiner Homepage zu Testzwecken verwendet werden.

```html
<!DOCTYPE html>
<html lang="de">
<head>
<meta charset="utf-8">
<title>Gutschein Fotoshooting</title>
<link rel="stylesheet" href="https://fonts.googleapis.com/css2?family=Yellowtail&family=Arimo&family=Quicksand:wght@300;400&display=swap">
<style>
  :root {
    --page: #ffffff;
    --frame: #dcdcdc;
    --card-dark: #2a211d;
    --card-mid: #4a3d36;
    --card-light: #6a5a50;
    --title: #8e8782;
    --text: #f2eeea;
    --field: rgba(230, 226, 224, 0.62);
    --field-text: #6a625d;
    --photo-border: #a8917d;
    --sparkle: #ffffff;
  }
  * { box-sizing: border-box; margin: 0; padding: 0; }
  html, body {
    width: 1200px; height: 655px; overflow: hidden;
    background: var(--page);
  }
  .canvas { position: relative; width: 1200px; height: 655px; }

  .card {
    position: absolute; top: 45px; width: 566px; height: 566px;
    background: var(--frame); padding: 10px;
    box-shadow: 2px 3px 6px rgba(0,0,0,0.25);
  }
  .card--front { left: 23px; }
  .card--back { left: 610px; }
  .card__face {
    position: relative; width: 100%; height: 100%; overflow: hidden;
  }
  .card__pattern {
    position: absolute; inset: 0;
    background: radial-gradient(ellipse at 50% 45%, var(--card-light) 0%, var(--card-mid) 45%, var(--card-dark) 100%);
  }

  .voucher-title {
    position: absolute; top: 42px; left: 0; right: 0; text-align: center;
    font-family: "Yellowtail", cursive; font-size: 104px; line-height: 1;
    color: var(--title);
  }
  .voucher-subtitle {
    position: absolute; top: 168px; left: 0; right: 0; text-align: center;
    font-family: "Arimo", sans-serif; font-size: 24px; color: var(--text);
  }

  .gallery { position: absolute; top: 222px; left: 0; right: 0; height: 200px; }
  .gallery__photo {
    position: absolute; border: 4px solid var(--photo-border); border-radius: 12px;
    box-shadow: 0 2px 6px rgba(0,0,0,0.5);
  }
  .gallery__photo--portrait {
    left: 38px; top: 14px; width: 148px; height: 178px; transform: rotate(-3deg);
    background: linear-gradient(160deg, #3b3f55 0%, #7a5c5a 50%, #d6b2a0 100%);
  }
  .gallery__photo--couple {
    left: 204px; top: 6px; width: 150px; height: 186px;
    background: linear-gradient(170deg, #2c5d9a 0%, #c9a58a 55%, #efe0c8 100%);
  }
  .gallery__photo--child {
    left: 374px; top: 12px; width: 160px; height: 178px; transform: rotate(3deg);
    background: linear-gradient(160deg, #dcc8a0 0%, #e6c1a6 50%, #b9c6d8 100%);
  }

  .studio-address {
    position: absolute; top: 425px; left: 0; right: 0; text-align: center;
    font-family: "Quicksand", sans-serif; font-weight: 300; font-size: 21px;
    line-height: 26px; color: var(--text);
  }

  .fields { position: absolute; top: 60px; left: 72px; width: 400px; }
  .field {
    height: 45px; margin-bottom: 24px; border-radius: 10px;
    background: var(--field); padding: 0 16px;
    font-family: "Quicksand", sans-serif; font-size: 17px; line-height: 45px;
    color: var(--field-text);
  }
  .photographer-photo {
    position: absolute; left: 165px; top: 283px; width: 212px; height: 211px;
    border-radius: 10px;
    background: linear-gradient(135deg, #cfcfcf 0%, #7a7a7a 45%, #1e1e1e 100%);
  }
  .website {
    position: absolute; top: 504px; left: 0; right: 0; text-align: center;
    font-family: "Quicksand", sans-serif; font-weight: 300; font-size: 20px;
    color: var(--text);
  }
  .sparkle { position: absolute; width: 54px; height: 54px; }
  .sparkle--front { left: 8px; top: 400px; }
  .sparkle--back { left: 450px; top: 34px; }
</style>
</head>
<body>
<div class="canvas">
  <section class="card card--front">
    <div class="card__face">
      <div class="card__pattern" role="img" aria-label="Dunkelbraunes Damast-Ornamentmuster"></div>
      <h1 class="voucher-title">Gutschein</h1>
      <p class="voucher-subtitle">für ein Fotoshooting</p>
      <div class="gallery">
        <div class="gallery__photo gallery__photo--portrait" role="img" aria-label="Foto: Porträt einer Frau mit Schmuck"></div>
        <div class="gallery__photo gallery__photo--couple" role="img" aria-label="Foto: Pärchen im Sommer"></div>
        <div class="gallery__photo gallery__photo--child" role="img" aria-label="Foto: lachendes Kind"></div>
      </div>
      <svg class="sparkle sparkle--front" viewBox="0 0 54 54" aria-hidden="true">
        <path d="M27 4 L29 25 L50 27 L29 29 L27 50 L25 29 L4 27 L25 25 Z" fill="var(--sparkle)" opacity="0.9"/>
      </svg>
      <address class="studio-address">
        Lukas Brandtner<br>
        Lindenhofgasse 7<br>
        4820 Talheim
      </address>
    </div>
  </section>

  <section class="card card--back">
    <div class="card__face">
      <div class="card__pattern" role="img" aria-label="Dunkelbraunes Damast-Ornamentmuster"></div>
      <div class="fields">
        <div class="field">Für</div>
        <div class="field">Wert</div>
        <div class="field">Datum, Unterschrift</div>
      </div>
      <svg class="sparkle sparkle--back" viewBox="0 0 54 54" aria-hidden="true">
        <path d="M27 4 L29 25 L50 27 L29 29 L27 50 L25 29 L4 27 L25 25 Z" fill="var(--sparkle)" opacity="0.9"/>
      </svg>
      <div class="photographer-photo" role="img" aria-label="Schwarzweiß-Foto: Fotograf mit Kamera"></div>
      <p class="website">www.lukasbrandtner.com</p>
    </div>
  </section>
</div>
</body>
</html>
```